RTV CRAFTED

building services
decks
pergola
renovation
extensions
general building

Target Market(s)

middle to upper class

Industry/Entity Type

building

Contact Information for Business Card

my details 0427839152 pkharlow47@mailvane.net BLD574926

Font styles to use
Serif

Colors
00AB8E
00BBA5
67D7C9
C6EFE9
E9F9F6

Requirements
Must have
• logo on the front and details on the back
Nice to have
• sharp and clean lines

```html
<!DOCTYPE html>
<html lang="en">
<head>
<meta charset="UTF-8">
<title>RTV CRAFTED – Business Cards</title>
<link href="https://fonts.googleapis.com/css2?family=Arimo:wght@400;700&display=swap" rel="stylesheet">
<style>
  :root {
    --bg: #1f1f1f;
    --card: #0b0b0b;
    --teal: #00ab8e;
    --teal-bright: #00bba5;
    --white: #ffffff;
    --rule: #3a3a3a;
  }
  * { margin: 0; padding: 0; box-sizing: border-box; }
  html, body {
    width: 1200px; height: 900px; overflow: hidden;
    background: var(--bg);
    font-family: "Arimo", Arial, sans-serif;
    color: var(--white);
  }
  .canvas {
    width: 1200px; height: 900px;
    display: flex; align-items: center; justify-content: center; gap: 40px;
  }
  .card {
    width: 540px; height: 310px;
    background: var(--card);
    position: relative;
    box-shadow: 0 14px 30px rgba(0,0,0,.55);
  }
  .wordmark {
    display: flex; align-items: center; gap: 10px;
    font-weight: 400; color: var(--white); letter-spacing: 0.5px;
    white-space: nowrap;
  }
  .wordmark-dot { width: 11px; height: 11px; background: var(--teal); flex: none; }

  /* details side */
  .card-details .wordmark {
    position: absolute; left: 34px; top: 50%; transform: translateY(-50%);
    font-size: 25px;
  }
  .divider {
    position: absolute; left: 292px; top: 78px; width: 1px; height: 154px;
    background: var(--rule);
  }
  .details { position: absolute; left: 314px; top: 86px; }
  .person-name { color: var(--teal-bright); font-weight: 700; font-size: 21px; line-height: 1.05; }
  .person-role { font-size: 14px; margin-bottom: 16px; }
  .contact-line {
    display: flex; align-items: center; gap: 8px;
    font-size: 13.5px; line-height: 1.55; white-space: nowrap;
  }
  .contact-line svg { width: 14px; height: 14px; flex: none; }
  .licence { margin-top: 14px; font-size: 14px; }
  .licence-prefix { color: var(--teal-bright); }

  /* services side */
  .card-services {
    display: flex; flex-direction: column; align-items: center; justify-content: center;
  }
  .card-services .wordmark { font-size: 42px; margin-bottom: 34px; }
  .services { text-align: center; font-size: 13.5px; line-height: 1.45; }
  .services .sep { color: var(--teal-bright); font-weight: 700; margin: 0 4px; }
</style>
</head>
<body>
<main class="canvas">
  <section class="card card-details" aria-label="Business card details side">
    <div class="wordmark"><span class="wordmark-dot"></span>RTV CRAFTED</div>
    <div class="divider"></div>
    <div class="details">
      <p class="person-name">Marcus Hale</p>
      <p class="person-role">Managing Director</p>
      <p class="contact-line">
        <svg viewBox="0 0 24 24" aria-hidden="true"><path fill="#00bba5" d="M6.6 10.8a15.1 15.1 0 0 0 6.6 6.6l2.2-2.2a1 1 0 0 1 1-.25 11.4 11.4 0 0 0 3.6.57 1 1 0 0 1 1 1V20a1 1 0 0 1-1 1A17 17 0 0 1 3 4a1 1 0 0 1 1-1h3.5a1 1 0 0 1 1 1c0 1.250.2 2.450.57 3.57a1 1 0 0 1-.25 1z"/></svg>
        0427839152
      </p>
      <p class="contact-line">
        <svg viewBox="0 0 24 24" aria-hidden="true"><path fill="#00bba5" d="M2 5h20v14H2z"/><path fill="none" stroke="#0b0b0b" stroke-width="1.8" d="M2 5l10 8 10-8"/></svg>
        pkharlow47@mailvane.net
      </p>
      <p class="licence"><span class="licence-prefix">BLD</span>574926</p>
    </div>
  </section>

  <section class="card card-services" aria-label="Business card front side">
    <div class="wordmark"><span class="wordmark-dot"></span>RTV CRAFTED</div>
    <div class="services">
      <p>Building Services<span class="sep">›</span>DecksPergola<span class="sep">›</span>Renovation</p>
      <p>Extensions<span class="sep">›</span>General Building</p>
    </div>
  </section>
</main>
</body>
</html>
```